Epoxy Flooring Contractor business card

We need a business card to promote a new addition to our business. We now offer Epoxy Flooring. We would like for the business card to include the images attached. One is our logo, the other is a sample of metallic epoxy flooring, we would like to incorporate that somewhere into the design. I was thinking an icon of a man pushing a concrete grinder and have the color set to the metallic epoxy color. I found a business card sample on this website, I will attach it. It has the icon that we are looking for, or something similar.
Our company name is Harborline Coatings LLC
Our owners name is Dane Morrow
Phone is 561-482-7160
website is www.harborline-coatingsllc.example
please let me know if you need any other info

Contact Information for Business Card

Harborline Coatings LLC
Dane Morrow, owner
Phone: 561-482-7160
Address: P.O Box 8241 Lake Worth, FL 33467
www.Harborline-CoatingsLLC.example
HarborlineCoatingsLLC@mailbox.example
Include logo attached
It must include a Clip art of man with concrete grinder
Must include metallic epoxy design attached
Must include the following text
Residential Garage Flooring
Epoxy Countertops
Commercial Epoxy Flooring
Restaurant Flooring
Warehouse Flooring
Licensed & Insured
Free Estimates

Colors

Designer to choose colors to be used in the design.

Requirements
Must have
• Include logo attached
• It must include a Clip art of man with concrete grinder
• Must include metallic epoxy design attached
• Must include the following text
• Garage Epoxy Flooring
• Residential Epoxy Flooring
• Concrete Floor Crack Repairs
• Concrete Floor Grinding
• Commercial & Warehouse Epoxy Flooring
• Restaurant Epoxy Flooring
• Epoxy Countertops
• Non Slip Epoxy Pool Decks
• Textured Finishes, Flakes, Granite Coat, Metallic & Quartz
• FREE ESTIMATES • LICENSED & INSURED

```html
<!DOCTYPE html>
<html lang="en">
<head>
<meta charset="utf-8">
<title>Harborline Coatings LLC – Business Card</title>
<link rel="stylesheet" href="https://fonts.googleapis.com/css2?family=Montserrat:wght@500&family=Raleway:ital,wght@1,300;1,400&display=swap">
<style>
  :root {
    --epoxy-deep: #1f4fa3;
    --epoxy-mid: #2f66bd;
    --epoxy-light: #5a8fd6;
    --epoxy-shadow: #173f86;
    --ink-white: #ffffff;
    --figure-tone: #eef3fb;
  }
  * { margin: 0; padding: 0; box-sizing: border-box; }
  html, body {
    width: 1200px;
    height: 720px;
    overflow: hidden;
    background: var(--epoxy-deep);
  }
  .card {
    position: relative;
    width: 1200px;
    height: 720px;
    overflow: hidden;
    color: var(--ink-white);
  }
  .metallic-epoxy {
    position: absolute;
    inset: 0;
    background:
      radial-gradient(ellipse 420px 260px at 15% 20%, rgba(90,143,214,0.55), transparent 70%),
      radial-gradient(ellipse 380px 240px at 80% 75%, rgba(90,143,214,0.45), transparent 70%),
      radial-gradient(ellipse 500px 300px at 55% 45%, rgba(23,63,134,0.45), transparent 70%),
      radial-gradient(ellipse 300px 200px at 90% 15%, rgba(23,63,134,0.5), transparent 70%),
      linear-gradient(160deg, var(--epoxy-mid) 0%, var(--epoxy-deep) 55%, var(--epoxy-mid) 100%);
  }
  .brand {
    position: absolute;
    left: 300px;
    top: 205px;
    display: flex;
    align-items: center;
    gap: 30px;
  }
  .brand-square {
    width: 100px;
    height: 100px;
    background: var(--ink-white);
  }
  .brand-name {
    font-family: 'Montserrat', sans-serif;
    font-weight: 500;
    font-size: 46px;
    line-height: 56px;
    letter-spacing: 1.5px;
    color: var(--ink-white);
  }
  .grinder-figure {
    position: absolute;
    left: 731px;
    top: 107px;
    width: 250px;
    height: 202px;
    border-radius: 10px;
    background: linear-gradient(180deg, rgba(238,243,251,0.85), rgba(238,243,251,0.6));
  }
  .services {
    position: absolute;
    left: 0;
    top: 375px;
    width: 1200px;
    list-style: none;
    font-family: 'Raleway', sans-serif;
    font-style: italic;
    font-weight: 400;
    font-size: 25px;
    text-align: center;
  }
  .services li {
    height: 50px;
    line-height: 50px;
    white-space: nowrap;
  }
  .services span { margin: 0 10px; }
  .services span::before {
    content: "\2022";
    font-style: normal;
    margin-right: 8px;
  }
  .services .assurances { font-weight: 300; letter-spacing: 0.3px; }
</style>
</head>
<body>
  <div class="card">
    <div class="metallic-epoxy" role="img" aria-label="Blue metallic epoxy floor texture"></div>

    <div class="brand">
      <div class="brand-square"></div>
      <div class="brand-name">Harborline<br>Coatings</div>
    </div>

    <div class="grinder-figure" role="img" aria-label="White silhouette of a worker pushing a concrete floor grinder"></div>

    <ul class="services">
      <li><span>Garage Epoxy Flooring</span><span>Residential Epoxy Flooring</span><span>Restaurant Epoxy Flooring</span></li>
      <li><span>Concrete Floor Crack Repairs</span><span>Concrete Floor Grinding</span><span>Epoxy Countertops</span></li>
      <li><span>Non Slip Epoxy Pool Decks</span><span>Commercial &amp; Warehouse Epoxy Flooring</span></li>
      <li><span>Textured Finishes, Flakes, Granite Coat, Metallic &amp; Quartz</span></li>
      <li class="assurances"><span>FREE ESTIMATES</span><span>LICENSED &amp; INSURED</span></li>
    </ul>
  </div>
</body>
</html>
```